Tovarro Bay Grill buffet and restaurant sold by the pound

I need something cool but informative and with all my day to day menu and catering . I want something with a organic feel but that works well with my branding so far . Using my logo and Brazilian colors.
Menu
Lunch-Dinner
Make your Combination Plate(Salads, Hot Dishes and Churrasco Meats) Sold by the Pound!!!
Salads + Hot Dishes (Buffet only) $8.65 per/Lb
Churrasco Meats+Hot Dishes+Salads $9.85 per/Lb
Churrasco Meats ( Only Meat) $15.95 per/Lb

Drinks

Guarana/Diet $2.50 Fruit Juice(especials) $4.50
Zolt/Diet $2.00 Vitamina (Fruit+Milk) $5.00 Glimra/Diet $2.00 Ice Tea/ Diet $2.00

Breakfast
7am-10am
Frittata $8.00

French Baguette Sandwich $8.00
Build your own
Cheese(Havarti/mozzarella)/Tomatoes/onions/bacon/lettuce
Beef/Chicken / Lombinho( Pork file)

Dessert ( Specials) $?

Catering Menu
*Pork chops stuffed with Garlic $35.00 (serves 5)
* Chicken Pot Pie Medium $60 (serves 8)
Large good for 15 people $110
*Chicken on Mango Sauce $34(serves 5)
*Eggplant Lasagna with banana Medium$30( serves 6)
Large $60 (serves 12)
*Try-tip stuffed with Bacon $53 (serves 5)
* Bacalhau ( dried cod fish) Chef style Medium $60( serve 6)
Large $120 (serves 14)
*Passion Fruit Mousse 320 ounce $25
*Strawberry Truffle Pie 320 ounce $30

• Menu
• Lunch-Dinner
• Make your Combination Plate(Salads, Hot Dishes and Churrasco Meats) Sold by the Pound!!!
• Salads + Hot Dishes (Buffet only) $8.65 per/Lb
• Churrasco Meats+Hot Dishes+Salads $9.85 per/Lb
• Churrasco Meats ( Only Meat) $15.95 per/Lb
• Drinks
• Guarana/Diet $2.50 Fruit Juice(specials menu) $4.50
• Zolt/Diet $2.00 Vitamin (Fruit+Milk) $5.00 Glimra/Diet $2.00 Ice Tea/ Diet $2.00
• Breakfast
• 7am-10am
• Frittata $8.00
• French Baguette Sandwich $8.00
• Build your own
• Cheese(Havarti/mozzarella)/Tomatoes/onions/bacon/lettuce
• Beef/Chicken / Lombinho( Pork file)
• Dessert ( Specials Menu) $?
• Catering Menu
• *Pork chops stuffed with Garlic serves 4-5 $35.00
• * Chicken Pot Pie serves 7-8 $60
• serves 14-15 $110
• *Chicken on Mango Sauce serves 4-5 $34
• *Eggplant Lasagna with banana serves 5-6 $30
• serves 12 - 13 $60
• *Try-tip stuffed with Bacon serves 4-5 $53
• * Bacalhau ( dried cod fish) Chef style serves 5-6 $60
• serves 14-15 $120
• *Passion Fruit Mousse 320 ounce $25
• *Strawberry Truffle Pie 320 ounce $30

```html
<!DOCTYPE html>
<html lang="en">
<head>
<meta charset="utf-8">
<title>Tovarro Bay Grill – Menu</title>
<link href="https://fonts.googleapis.com/css2?family=Chewy&family=Patrick+Hand&display=swap" rel="stylesheet">
<style>
  :root {
    --backdrop: #595959;
    --green-deep: #07702f;
    --green-mid: #129a45;
    --green-light: #1fae55;
    --yellow: #e8d52c;
    --yellow-rule: #f2c500;
    --navy: #1c2f5e;
    --ink-light: #ffffff;
    --ink-dark: #0f3d3f;
    --sky-top: #bfe2f6;
    --sky-mid: #8dbde0;
    --bay: #3e74b0;
    --city: #7d8e9e;
    --hill: #3d6a45;
    --heading-font: "Chewy", cursive;
    --body-font: "Patrick Hand", cursive;
  }
  * { margin: 0; padding: 0; box-sizing: border-box; }
  html, body { width: 1200px; height: 738px; overflow: hidden; background: var(--backdrop); }
  .canvas { position: relative; width: 1200px; height: 738px; }

  .page { position: absolute; top: 40px; width: 471px; height: 659px; overflow: hidden; }
  .page--cover { left: 111px; }
  .page--menu {
    left: 643px;
    background: radial-gradient(ellipse at 50% 45%, var(--green-light) 0%, var(--green-mid) 45%, var(--green-deep) 100%);
    color: var(--ink-light);
    font-family: var(--body-font);
  }

  /* Cover */
  .cover-photo {
    position: absolute; inset: 0;
    background: linear-gradient(180deg, var(--sky-top) 0%, var(--sky-mid) 24%, var(--bay) 42%, var(--city) 60%, var(--hill) 80%);
  }
  .brand-name {
    position: absolute; top: 120px; left: 0; width: 100%;
    text-align: center;
    font-family: var(--heading-font);
    font-size: 38px; color: var(--ink-dark);
  }
  .cover-band { position: absolute; left: 0; top: 420px; width: 471px; height: 239px; }
  .cover-info {
    position: absolute; left: 0; top: 485px; width: 452px;
    text-align: center; color: var(--ink-light); font-family: var(--body-font);
  }
  .cover-title { font-family: var(--heading-font); color: var(--yellow); font-size: 31px; line-height: 1; }
  .cover-subtitle { font-family: var(--heading-font); color: var(--yellow); font-size: 19px; line-height: 1.1; margin-bottom: 10px; }
  .cover-address { font-size: 14px; line-height: 1.2; }
  .cover-contact { font-size: 14px; line-height: 1.25; margin-top: 8px; }
  .cover-contact svg { width: 10px; height: 10px; fill: var(--yellow); vertical-align: -1px; margin-right: 4px; }
  .sold-badge {
    position: absolute; left: 367px; top: 459px; width: 62px; height: 85px;
    background: var(--navy); color: var(--yellow);
    font-family: var(--body-font); font-size: 15px; line-height: 1.15;
    display: flex; align-items: center; justify-content: center; text-align: center;
  }

  /* Menu */
  .section-title {
    position: absolute; left: 0; width: 100%; text-align: center;
    font-family: var(--heading-font); color: var(--yellow); font-size: 24px; line-height: 1;
  }
  .section-title span { display: inline-block; padding: 0 4px 2px; border-bottom: 1px solid var(--yellow); }
  .centered { position: absolute; left: 0; width: 100%; text-align: center; }
  .combo-title { font-size: 17px; line-height: 1; }
  .small-note { font-size: 9px; line-height: 1; }
  .hours { font-size: 21px; line-height: 1; }
  .build-text { font-size: 10px; line-height: 12.5px; }

  .price-list { position: absolute; left: 46px; width: 379px; list-style: none; }
  .price-row { display: flex; align-items: center; height: 13.4px; font-size: 10px; white-space: nowrap; }
  .price-row .item { flex: none; }
  .price-row .leader { flex: 1; height: 1px; background: var(--ink-light); opacity: .85; margin: 2px 4px 0; }
  .price-row .price { flex: none; }
  .catering .price-row { position: relative; height: 13.1px; }
  .catering .serves { position: absolute; left: 238px; width: 80px; text-align: center; font-size: 8px; top: -2px; background: transparent; }
</style>
</head>
<body>
<div class="canvas">

  <section class="page page--cover">
    <div class="cover-photo" role="img" aria-label="Photo of Rio de Janeiro bay with Sugarloaf Mountain and the hilltop statue overlooking the city"></div>
    <div class="brand-name">Tovarro Bay Grill</div>
    <svg class="cover-band" viewBox="0 0 471 239" aria-hidden="true">
      <defs>
        <linearGradient id="bandGreen" x1="0" y1="0" x2="0" y2="1">
          <stop offset="0" stop-color="#129a45"/>
          <stop offset="1" stop-color="#07702f"/>
        </linearGradient>
      </defs>
      <polygon points="0,76 236,8 471,76 471,239 0,239" fill="url(#bandGreen)"/>
      <polyline points="0,76 236,8 471,76" fill="none" stroke="#f2c500" stroke-width="4"/>
    </svg>
    <div class="cover-info">
      <h1 class="cover-title">Brazilian BBQ</h1>
      <p class="cover-subtitle">Buffet Restaurant</p>
      <p class="cover-address">1850 west marlow blvd, ste. E<br>Calderon Park, Ca 90000</p>
      <p class="cover-contact">
        <svg viewBox="0 0 10 10"><path d="M2 0h2l1 3-1.5 1a6 6 0 0 0 2.5 2.5L7 5l3 1v2c0 1-1 2-2 2C4 10 0 6 0 2 0 1 1 0 2 0z"/></svg>5550142287<br>
        <svg viewBox="0 0 10 10"><path d="M0 2h10v6H0z M0 2l5 3.5L10 2" stroke="#07702f" stroke-width=".8"/></svg>tovarrobaygrill@mailbox.com
      </p>
    </div>
    <div class="sold-badge">Sold<br>By The<br>Pound!!!</div>
  </section>

  <section class="page page--menu">
    <h2 class="section-title" style="top:30px"><span>Lunch-Dinner</span></h2>
    <p class="centered combo-title" style="top:60px">Make your Combination Plate</p>
    <p class="centered small-note" style="top:79px">(Salads, Hot Dishes and Churrasco Meats)</p>
    <ul class="price-list" style="top:98px">
      <li class="price-row"><span class="item">Salads + Hot Dishes (Buffet only)</span><span class="leader"></span><span class="price">$8.65 per/Lb</span></li>
      <li class="price-row"><span class="item">Churrasco Meats+Hot Dishes+Salads</span><span class="leader"></span><span class="price">$9.85 per/Lb</span></li>
      <li class="price-row"><span class="item">Churrasco Meats ( Only Meat)</span><span class="leader"></span><span class="price">$15.95 per/Lb</span></li>
    </ul>

    <h2 class="section-title" style="top:152px"><span>Drinks</span></h2>
    <ul class="price-list" style="top:177px">
      <li class="price-row"><span class="item">Guarana/Diet</span><span class="leader"></span><span class="price">$2.50</span></li>
      <li class="price-row"><span class="item">Fruit Juice(especials)</span><span class="leader"></span><span class="price">$4.50</span></li>
      <li class="price-row"><span class="item">Zolt/Diet</span><span class="leader"></span><span class="price">$2.00</span></li>
      <li class="price-row"><span class="item">Vitamina (Fruit+Milk)</span><span class="leader"></span><span class="price">$5.00</span></li>
      <li class="price-row"><span class="item">Glimra/Diet</span><span class="leader"></span><span class="price">$2.00</span></li>
      <li class="price-row"><span class="item">Ice Tea/ Diet</span><span class="leader"></span><span class="price">$2.00</span></li>
    </ul>

    <h2 class="section-title" style="top:272px"><span>Breakfast</span></h2>
    <p class="centered hours" style="top:300px">7am-10am</p>
    <ul class="price-list" style="top:323px">
      <li class="price-row"><span class="item">Frittata</span><span class="leader"></span><span class="price">$8.00</span></li>
      <li class="price-row"><span class="item">French Baguette Sandwich</span><span class="leader"></span><span class="price">$8.00</span></li>
    </ul>
    <p class="centered build-text" style="top:353px">Build your own<br>Cheese(Havarti/mozzarella)/Tomatoes/onions/bacon/lettuce<br>Beef/Chicken / Lombinho( Pork file)</p>
    <ul class="price-list" style="top:406px">
      <li class="price-row"><span class="item">Dessert ( Specials)</span><span class="leader"></span><span class="price">$&nbsp;&nbsp;&nbsp;&nbsp;&nbsp;&nbsp;&nbsp;&nbsp;</span></li>
    </ul>

    <h2 class="section-title" style="top:443px"><span>Catering Menu</span></h2>
    <ul class="price-list catering" style="top:479px">
      <li class="price-row"><span class="item">Pork chops stuffed with Garlic</span><span class="leader"></span><span class="serves">(serves 5)</span><span class="price">$35.00</span></li>
      <li class="price-row"><span class="item">Chicken Pot Pie</span><span class="leader"></span><span class="serves">(serves 8)</span><span class="price">$60.00</span></li>
      <li class="price-row"><span class="item">Large good</span><span class="leader"></span><span class="serves">(serves 15)</span><span class="price">$110.00</span></li>
      <li class="price-row"><span class="item">Chicken on Mango Sauce</span><span class="leader"></span><span class="serves">(serves 5)</span><span class="price">$34.00</span></li>
      <li class="price-row"><span class="item">Eggplant Lasagna with banana</span><span class="leader"></span><span class="serves">(serves 6)</span><span class="price">$30.00</span></li>
      <li class="price-row"><span class="item"></span><span class="leader" style="margin-left:238px"></span><span class="serves">(serves 12)</span><span class="price">$60.00</span></li>
      <li class="price-row"><span class="item">Try-tip stuffed with Bacon</span><span class="leader"></span><span class="serves">(serves 5)</span><span class="price">$53.00</span></li>
      <li class="price-row"><span class="item">Bacalhau ( dried cod fish) Chef style</span><span class="leader"></span><span class="serves">(serves 6)</span><span class="price">$60.00</span></li>
      <li class="price-row"><span class="item"></span><span class="leader" style="margin-left:238px"></span><span class="serves">(serves 14)</span><span class="price">$120.00</span></li>
      <li class="price-row"><span class="item">Passion Fruit Mousse 320 ounce</span><span class="leader"></span><span class="price">$25.00</span></li>
      <li class="price-row"><span class="item">Strawberry Truffle Pie 320 ounce</span><span class="leader"></span><span class="price">$30.00</span></li>
    </ul>
  </section>

</div>
</body>
</html>
```